Velvet Quarry Powerpoint Presentation

Looking for powerpoint presentation template for our boutique social media management and digital marketing company.
We will be using this Powerpoint template for presentations, guest speaking sessions and proposals.
We need a front page and then a few different versions of what the rest of the template would look like.
I have attached our business cards, different versions of our logo, and our PDF so you can get a look at our identity and get a feel of what we are about. Our website will be up in about two weeks.
Target Market(s)
Small to medium size business owners (all different catagories)
Industry/Entity Type
Marketing
Requirements
Must have
- The logo
- a very boutique, high end look. You will see what I mean when you look at our business cards and our PDF.
- We only want to use the Velvet Quarry colors- Black, White, Rose Gold and Grey
Should not have
- Lot's of colors that are not part of the Velvet Quarry identity

```html
<!DOCTYPE html>
<html lang="en">
<head>
<meta charset="utf-8">
<title>Velvet Quarry – Presentation Cover</title>
<link rel="stylesheet" href="https://fonts.googleapis.com/css2?family=Cabin:wght@400;500&family=Montserrat:wght@300&display=swap">
<style>
  :root {
    --white: #ffffff;
    --rose: #f5d3c5;
    --rose-deep: #f0c4b2;
    --grey: #828282;
    --grey-text: #7d7d7d;
  }
  html, body {
    margin: 0;
    padding: 0;
    overflow: hidden;
    background: var(--white);
  }
  .cover {
    position: relative;
    width: 1200px;
    height: 900px;
    overflow: hidden;
    background: var(--white);
  }
  .brand {
    position: absolute;
    right: 33px;
    top: 318px;
    display: flex;
    align-items: center;
    gap: 18px;
  }
  .brand-dot {
    width: 22px;
    height: 22px;
    border-radius: 50%;
    background: var(--rose-deep);
  }
  .brand-name {
    margin: 0;
    font-family: "Montserrat", sans-serif;
    font-weight: 300;
    font-size: 56px;
    line-height: 1;
    letter-spacing: 1px;
    text-transform: uppercase;
    color: var(--grey);
  }
  .band {
    position: absolute;
    left: 0;
    top: 410px;
    width: 1200px;
    height: 490px;
    background: var(--rose);
  }
  .project {
    position: absolute;
    right: 36px;
    top: 570px;
    text-align: right;
  }
  .project-title {
    margin: 0 0 22px;
    font-family: "Cabin", sans-serif;
    font-weight: 500;
    font-size: 45px;
    line-height: 1;
    color: var(--grey);
  }
  .project-subtext {
    margin: 0;
    width: 440px;
    margin-left: auto;
    font-family: "Cabin", sans-serif;
    font-weight: 400;
    font-size: 21px;
    line-height: 37.5px;
    color: var(--grey-text);
  }
</style>
</head>
<body>
  <main class="cover">
    <header class="brand">
      <span class="brand-dot" aria-hidden="true"></span>
      <h1 class="brand-name">Velvet Quarry</h1>
    </header>
    <section class="band">
    </section>
    <section class="project">
      <h2 class="project-title">PROJECT TITLE HERE</h2>
      <p class="project-subtext">Subtext here Subtext here Subtext here Subtext here Subtext here Subtext here Subtext here Subtext here</p>
    </section>
  </main>
</body>
</html>
```